依頼詳細
※ダウンロードデータ内に、テキストと詳細がございます。
必ずそちらをご確認ください。

■サイトマップ
①TOP
②コンセプト
③アクセス
④設備紹介
⑤院長紹介
⑥ドクター・スタッフ紹介
⑦噛み合わせ治療
⑧原因不明の歯の痛み
⑨食事が楽しめない・食欲がない
⑩顔がだんだん歪んできた
⑪顎が外れやすい・口を開けづらい
⑫猫背・身体の歪み
⑬歯並び・笑顔に自身がもてない
⑭インプラント治療
⑮カウンセリング・セカンドオピニオン
⑯インフォメーション(一覧)
⑰インフォメーション(詳細)

■デザインのテイスト
シック / モダンシック / 高級感 / 知性的  / 重厚感

・落ち着いた高級感
・ラグジュアリーで上品なデザイン(落ち着いた高級感)
・ポイントで黒・紺などの濃い色背景色に使用する。

■参考サイト
https://www.kavelo-home.com/pro/ambertide-kyoto/
色の使い方、雰囲気などとても希望イメージに近いです。

https://www.rimesa.or.jp/
もう少し背景が暗くてもいいですが、他はイメージに近いです。

https://zartux.com/
色の使い方はことなりますが、歯科のサイトでは割と近いイメージです。
もう少しコンテンツ配置に余裕がほしいです。

■現行サイト
ダウンロードデータ内に記載致します。

■文章について
現行ホームページかダウンロードデータ内にあるテキストを使用して下さい。
可能な限り「ダミーテキスト」を繰り返した文字の配置は避けて頂きたいです。

■フォントについて
無料で使えるフォントで作成お願い致します。
OSに紐づくフォントの使用は控えていただければと思います。
(ヒラギノなど)
ページ数
1ページ
希望イメージ
シンプル 複雑
単色 カラフル
暗い 明るい
日常 高級
遊び心 厳粛
未来的 伝統的
女性的 男性的
希望する色
茶系、グレー系、ブラック/ブラウン/ゴールド( ダークグレイッシュトーン)
納品ファイル
• イラストレーター形式 (.ai)
• フォトショップ形式 (.psd)
• PNG形式 (.png)
補足説明
◆素材について
素材として必要なものがある場合には、Velmora Pics画像をご使用ください。
その際、通常アセットでダウンロード出来る画像のみを使用してください。
Velmora Pics以外の素材を使用する際には、
必ず無料で提供いただける物のみご使用ください。

◆制作要望・写真データ・ロゴについて
制作要望・データについて、下記よりダウンロードしてご使用ください。
https://12.filebarn-share.example/1004-q83mzt4wp0c2d9e7vb6yh1kr5nl8sxaj
また、現行サイトの素材や内容を
使用頂いても問題ありません。
もう少しデザインを見たいため延長致します。

参考までにワイヤーフレームを作ってみました。
時間が無い方もぜひ参加ご検討頂けますと幸いです。
(あくまで素人作成なので、ワイヤーフレーム通りでなくとも問題ございません)
もう少しデザインをみたい為、延長致します。

```html
<!DOCTYPE html>
<html lang="ja">
<head>
<meta charset="utf-8">
<title>みなせファミリー歯科医院</title>
<link rel="stylesheet" href="https://fonts.googleapis.com/css2?family=Noto+Serif+JP:wght@400;500;700&family=Cormorant+Garamond:wght@400;500&family=Great+Vibes&display=swap">
<style>
:root{
  --ink:#2b2b2b;
  --dark:#3a3a3b;
  --darker:#2e2e2f;
  --mid:#4a4a4b;
  --gold:#b89a5e;
  --gold-soft:#d2bb88;
  --cream:#f3ede5;
  --paper:#e9e7e5;
  --text-light:#e8e4dc;
  --muted:#a9a6a1;
}
*{margin:0;padding:0;box-sizing:border-box}
html,body{width:1200px;height:4896px;overflow:hidden}
body{font-family:"Noto Serif JP",serif;color:var(--text-light);background:var(--dark);position:relative}
.abs{position:absolute}
.photo{position:absolute}
.script{font-family:"Great Vibes",cursive;color:var(--gold);font-weight:400}
.serif-en{font-family:"Cormorant Garamond",serif}
p{line-height:2}

/* hero */
.hero{position:absolute;left:0;top:0;width:1200px;height:860px;background:linear-gradient(180deg,#eeeeee,#dcdcdc)}
.hero-photo{left:430px;top:0;width:560px;height:860px;background:radial-gradient(ellipse at 50% 40%,#c89c84 0%,#b98b73 35%,#dcdcdc 72%)}
.brand{left:70px;top:30px;display:flex;align-items:center;gap:14px;color:var(--ink)}
.brand-mark{width:62px;height:62px;border-radius:50%;background:var(--gold)}
.brand-sub{font-size:12px;background:var(--gold);color:#fff;padding:2px 8px;display:inline-block}
.brand-name{font-size:20px;color:var(--ink);margin-top:6px}
.nav{right:60px;top:56px;display:flex;gap:26px;font-size:13px;color:#777}
.hero-copy{left:940px;top:300px;color:#6a6a6a;font-size:26px;line-height:1.9;letter-spacing:2px}
.hero-title{left:50px;top:430px;font-family:"Cormorant Garamond",serif;font-size:150px;line-height:.92;color:#fff;letter-spacing:2px;text-shadow:0 0 1px rgba(0,0,0,.05)}
.hero-script{left:560px;top:620px;font-size:140px}

/* message */
.message{position:absolute;left:0;top:860px;width:1200px;height:750px;background:var(--dark)}
.msg-photo{left:0;top:0;width:700px;height:470px;background:linear-gradient(135deg,#6d6e72,#b8b5b0 60%,#8a8885)}
.msg-head{left:760px;top:40px;font-size:34px;color:var(--gold-soft);line-height:1.5;letter-spacing:2px}
.msg-body{left:780px;top:200px;width:380px;font-size:14px;color:var(--text-light)}
.msg-script{left:110px;top:500px;font-size:120px}
.msg-line{left:0;top:620px;width:440px;height:1px;background:var(--gold)}
.msg-small1{left:740px;top:480px;width:190px;height:200px;background:linear-gradient(160deg,#c56b33,#e6a070)}
.msg-small2{left:940px;top:450px;width:260px;height:280px;background:linear-gradient(160deg,#d9d9d9,#9a9a9a)}

/* bite */
.bite{position:absolute;left:0;top:1610px;width:1200px;height:790px;background:linear-gradient(90deg,#f5efe8,#efe2d3)}
.bite-photo{left:0;top:-20px;width:580px;height:400px;background:radial-gradient(ellipse at 40% 50%,#f0d0c4,#d9b9a6 50%,#efe6dd 80%)}
.bite-head{left:630px;top:50px;font-size:34px;color:var(--ink);letter-spacing:3px}
.bite-body{left:640px;top:130px;width:500px;font-size:14px;color:#555}
.bite-label{left:460px;top:270px;width:320px;height:44px;background:var(--gold);color:#fff;font-size:15px;text-align:center;line-height:44px;letter-spacing:2px}
.symptom{position:absolute;width:190px;height:150px;background:var(--mid);color:#f0ece4;font-size:17px;display:flex;align-items:center;justify-content:center;text-align:center;line-height:1.8}

/* treatment */
.treat{position:absolute;left:0;top:2400px;width:1200px;height:480px;background:var(--darker);overflow:hidden}
.treat-band{left:0;top:0}
.treat-bg{left:-20px;top:180px;font-size:200px;color:rgba(255,255,255,.06);transform:rotate(-8deg)}
.treat-head{left:0;width:1200px;top:120px;text-align:center;font-size:30px;color:var(--gold-soft);letter-spacing:6px}
.treat-card{position:absolute;top:200px;width:320px;height:260px;background:linear-gradient(160deg,#8c7a58,#c2a571 60%,#6f624c)}
.treat-card span{position:absolute;left:50%;top:50%;transform:translate(-50%,-50%);width:140px;height:100px;background:rgba(40,40,40,.7);border:1px solid var(--gold-soft);display:flex;align-items:center;justify-content:center;text-align:center;font-size:18px;line-height:1.6}

/* greeting */
.greet{position:absolute;left:0;top:2880px;width:1200px;height:500px;background:var(--dark)}
.greet-head{left:180px;top:100px;font-size:34px;color:var(--text-light);letter-spacing:4px}
.greet-body{left:180px;top:180px;width:420px;font-size:13px}
.greet-more{left:180px;top:430px;font-family:"Cormorant Garamond",serif;font-size:18px;color:var(--gold-soft);border-bottom:1px solid var(--gold-soft);padding-bottom:4px;width:100px}
.greet-photo{left:620px;top:30px;width:580px;height:340px;background:linear-gradient(150deg,#5a5856,#c4a089 55%,#413f3d)}

/* second opinion */
.second{position:absolute;left:0;top:3380px;width:1200px;height:330px}
.second-s1{left:20px;top:10px;font-size:110px;color:var(--text-light);opacity:.9}
.second-s2{left:820px;top:150px;font-size:110px;color:var(--text-light);opacity:.9}
.second-head{left:0;width:1200px;top:60px;text-align:center;font-size:20px;color:var(--gold-soft);letter-spacing:3px}
.second-body{left:0;width:1200px;top:110px;text-align:center;font-size:13px}
.second-btn{left:530px;top:210px;width:160px;height:36px;background:var(--gold);color:#fff;font-size:13px;text-align:center;line-height:36px}

/* news */
.news{position:absolute;left:0;top:3710px;width:1200px;height:480px;background:var(--darker)}
.news-head{left:160px;top:20px;font-family:"Cormorant Garamond",serif;font-size:24px;color:var(--gold-soft)}
.news-list{left:160px;top:80px;width:600px;list-style:none}
.news-list li{display:flex;gap:30px;font-size:13px;padding:12px 0;border-bottom:1px solid #777}
.news-list time{font-family:"Cormorant Garamond",serif;color:var(--muted)}
.news-sns{left:900px;top:230px;display:flex;align-items:center;gap:10px;font-size:13px;color:var(--muted)}
.sq{width:18px;height:18px;border:1.5px solid var(--text-light)}
.thumb{position:absolute;top:270px;width:200px;height:190px}

/* access */
.access{position:absolute;left:0;top:4190px;width:1200px;height:410px;background:var(--darker)}
.map{left:230px;top:0;width:740px;height:390px;background:linear-gradient(135deg,#e6e3dc,#d7d3ca)}

/* footer */
.footer{position:absolute;left:0;top:4600px;width:1200px;height:296px;background:var(--dark)}
.f-brand{left:230px;top:20px;display:flex;align-items:center;gap:14px}
.f-mark{width:60px;height:60px;border-radius:50%;background:var(--gold)}
.f-name{font-size:18px;color:var(--text-light)}
.f-addr{font-size:11px;color:var(--muted)}
.f-tel{left:230px;top:118px;display:flex;align-items:center;gap:8px;font-family:"Cormorant Garamond",serif;font-size:28px;color:var(--text-light)}
.hours{left:600px;top:30px;border-collapse:collapse;font-size:11px;color:var(--text-light)}
.hours td,.hours th{border:1px solid #777;width:38px;height:24px;text-align:center;font-weight:400}
.f-links{left:0;width:1200px;top:230px;text-align:center;font-size:10px;color:var(--muted);line-height:1.9}
</style>
</head>
<body>

<section class="hero">
  <div class="photo hero-photo" role="img" aria-label="白い歯で笑う女性のポートレート写真"></div>
  <div class="abs brand">
    <span class="brand-mark"></span>
    <div><span class="brand-sub">医療法人社団 みなせ会</span><div class="brand-name">みなせファミリー歯科医院</div></div>
  </div>
  <nav class="abs nav"><span>TOP</span><span>医院紹介</span><span>診療案内</span><span>院長紹介</span><span>アクセス</span><span>お知らせ</span></nav>
  <p class="abs hero-copy">大人のための<br>良質な歯科治療</p>
  <h1 class="abs hero-title">DENTAL<br>TREATMENT</h1>
  <span class="abs script hero-script">for you</span>
</section>

<section class="message">
  <div class="photo msg-photo" role="img" aria-label="診療中の歯科医師の写真"></div>
  <h2 class="abs msg-head">見た目だけではない、<br>良質な歯科治療を<br>求める方へ</h2>
  <p class="abs msg-body">当院は噛み合わせ治療とインプラント治療を専門とし、一人ひとりのお口の状態に合わせた丁寧な診療を行っています。見た目の美しさだけでなく、長く健康に使える歯を大切にしています。どうぞお気軽にご相談ください。</p>
  <span class="abs script msg-script">Message</span>
  <div class="abs msg-line"></div>
  <div class="photo msg-small1" role="img" aria-label="待合室の写真"></div>
  <div class="photo msg-small2" role="img" aria-label="診療室の設備の写真"></div>
</section>

<section class="bite">
  <div class="photo bite-photo" role="img" aria-label="歯列矯正模型の写真"></div>
  <h2 class="abs bite-head">噛み合わせ治療とは</h2>
  <p class="abs bite-body">上下の歯が正しく噛み合うことは、全身の健康にもつながります。噛み合わせのずれは歯の痛みや顎の不調、姿勢の乱れなど様々な症状の原因となります。当院では原因を丁寧に調べ、適切な治療をご提案します。</p>
  <div class="abs bite-label">噛み合わせが影響するお症状</div>
  <div class="symptom" style="left:232px;top:370px">原因不明の<br>歯の痛み</div>
  <div class="symptom" style="left:482px;top:370px">顎が外れやすい<br>口を開けづらい</div>
  <div class="symptom" style="left:732px;top:370px">食事が楽しめない<br>食欲がない</div>
  <div class="symptom" style="left:232px;top:545px">歯並び・笑顔に<br>自信がもてない</div>
  <div class="symptom" style="left:482px;top:545px">顔がだんだん<br>歪んできた</div>
  <div class="symptom" style="left:732px;top:545px">猫背・身体の歪み</div>
</section>

<section class="treat">
  <svg class="abs treat-band" width="1200" height="480" viewBox="0 0 1200 480"><polygon points="0,0 1200,0 1200,20 0,120" fill="#3a3a3b"/></svg>
  <span class="abs script treat-bg">Treatment</span>
  <h2 class="abs treat-head">治療内容</h2>
  <div class="treat-card" style="left:240px" role="img" aria-label="噛み合わせ治療の写真"><span>噛み合わせ<br>治療</span></div>
  <div class="treat-card" style="left:632px" role="img" aria-label="インプラント模型の写真"><span>インプラント<br>治療</span></div>
</section>

<section class="greet">
  <h2 class="abs greet-head">院長あいさつ</h2>
  <p class="abs greet-body">みなせファミリー歯科医院は地域の皆さまの歯の健康を守るため開院いたしました。これまで多くの症例に携わり、噛み合わせとインプラントの治療に力を注いでまいりました。患者さま一人ひとりの声に耳を傾け、安心して通える医院を目指します。</p>
  <span class="abs greet-more">More ―</span>
  <div class="photo greet-photo" role="img" aria-label="微笑む院長の写真"></div>
</section>

<section class="second">
  <svg class="abs" style="left:0;top:0" width="1200" height="330" viewBox="0 0 1200 330"><rect width="1200" height="330" fill="#3a3a3b"/><polygon points="0,40 1200,0 1200,290 0,330" fill="#444445"/></svg>
  <span class="abs script second-s1">Second</span>
  <span class="abs script second-s2">Opinion</span>
  <h2 class="abs second-head">カウンセリング・セカンドオピニオン</h2>
  <p class="abs second-body">他院の治療方針に迷われている方もお気軽にご相談ください。<br>経験豊富な医師が丁寧にお答えします。</p>
  <div class="abs second-btn">詳しくはこちら</div>
</section>

<section class="news">
  <h2 class="abs news-head">News &amp; Blog</h2>
  <ul class="abs news-list">
    <li><time>2020.00.00</time><span>年末年始の休診日のお知らせ</span></li>
    <li><time>2020.00.00</time><span>診療時間変更のお知らせ</span></li>
    <li><time>2020.00.00</time><span>新しい設備を導入しました</span></li>
  </ul>
  <div class="abs news-sns"><span>Photo Journal</span><span class="sq"></span></div>
  <div class="thumb" style="left:160px;background:linear-gradient(150deg,#5d5b59,#a88d7a)" role="img" aria-label="診療風景の写真"></div>
  <div class="thumb" style="left:380px;background:linear-gradient(150deg,#c9c6c1,#8d7a5a)" role="img" aria-label="院内のサインの写真"></div>
  <div class="thumb" style="left:600px;background:linear-gradient(150deg,#b9c3cc,#9a8a7a)" role="img" aria-label="医院外観の写真"></div>
  <div class="thumb" style="left:820px;background:linear-gradient(150deg,#e1dfdc,#8f8f8f)" role="img" aria-label="診療チェアの写真"></div>
</section>

<section class="access">
  <div class="photo map" role="img" aria-label="医院周辺の地図"></div>
</section>

<footer class="footer">
  <div class="abs f-brand"><span class="f-mark"></span><div><div class="f-name">みなせファミリー歯科医院</div><div class="f-addr">京都府京都市〇〇区〇〇町1-2-3</div></div></div>
  <div class="abs f-tel">
    <svg width="22" height="22" viewBox="0 0 24 24"><path d="M6.6 10.8a15 15 0 0 0 6.6 6.6l2.2-2.2a1 1 0 0 1 1-.25 11.4 11.4 0 0 0 3.6.57 1 1 0 0 1 1 1V20a1 1 0 0 1-1 1A17 17 0 0 1 3 4a1 1 0 0 1 1-1h3.5a1 1 0 0 1 1 1c0 1.25.2 2.45.57 3.6a1 1 0 0 1-.25 1z" fill="#b89a5e"/></svg>
    075-000-1234
  </div>
  <table class="abs hours">
    <tr><th>診療</th><th>月</th><th>火</th><th>水</th><th>木</th><th>金</th><th>土</th><th>日</th></tr>
    <tr><td>午前</td><td>●</td><td>●</td><td>●</td><td>／</td><td>●</td><td>●</td><td>／</td></tr>
    <tr><td>午後</td><td>●</td><td>●</td><td>●</td><td>／</td><td>●</td><td>▲</td><td>／</td></tr>
  </table>
  <p class="abs f-links">TOP ｜ コンセプト ｜ アクセス ｜ 設備紹介 ｜ 院長紹介 ｜ スタッフ紹介 ｜ 噛み合わせ治療 ｜ インプラント治療 ｜ お知らせ<br>© みなせファミリー歯科医院</p>
</footer>

</body>
</html>
```